Business Card Design

Create three options for business cards based on the design and colors in the attached file.
Vectors are preferred
One of the options should use Rose Gold, and the others Yellow Gold

```html
<!DOCTYPE html>
<html lang="en">
<head>
<meta charset="utf-8">
<title>Arvelo Interior Decor — Business Card</title>
<link rel="stylesheet" href="https://fonts.googleapis.com/css2?family=Ubuntu:wght@400;700&display=swap">
<style>
  :root {
    --backdrop: #262626;
    --blush: #f5cdc6;
    --blush-soft: #f7d9d3;
    --slate: #7a7677;
    --slate-light: #b8a6a4;
    --gold: #d9a92a;
    --gold-soft: #e8c15a;
    --white: #ffffff;
  }
  * { box-sizing: border-box; margin: 0; padding: 0; }
  html, body {
    width: 1200px;
    height: 900px;
    overflow: hidden;
    background: var(--backdrop);
    font-family: "Ubuntu", "Helvetica Neue", Arial, sans-serif;
  }
  .stage {
    position: relative;
    width: 1200px;
    height: 900px;
    display: flex;
    flex-direction: column;
    align-items: center;
    justify-content: center;
    gap: 70px;
  }
  .card {
    position: relative;
    width: 560px;
    height: 320px;
    overflow: hidden;
  }

  /* Back side */
  .card-back {
    background: linear-gradient(180deg, var(--slate-light) 0%, var(--slate) 42%, var(--slate) 100%);
  }
  .contact-panel {
    position: absolute;
    left: 300px;
    top: 90px;
    width: 180px;
    height: 230px;
    background: var(--blush);
    display: flex;
    flex-direction: column;
    justify-content: flex-end;
    padding: 0 0 28px 18px;
    gap: 8px;
  }
  .contact-phone {
    color: var(--gold);
    font-size: 21px;
    font-weight: 400;
    letter-spacing: 0.5px;
  }
  .contact-email {
    color: var(--gold);
    font-size: 11px;
  }

  /* Front side */
  .card-front {
    background: var(--blush);
  }
  .dot-pattern {
    position: absolute;
    inset: 0;
    background:
      linear-gradient(155deg, rgba(232,193,90,0.0) 0%, rgba(232,193,90,0.45) 30%, rgba(245,205,198,0.2) 50%, rgba(232,193,90,0.45) 72%, rgba(245,205,198,0.1) 100%),
      var(--blush-soft);
  }
  .name-panel {
    position: absolute;
    left: 150px;
    top: 0;
    width: 230px;
    height: 190px;
    background: var(--slate);
    display: flex;
    flex-direction: column;
    justify-content: flex-end;
    padding: 0 0 24px 24px;
  }
  .name-first {
    color: var(--gold);
    font-weight: 700;
    font-size: 38px;
    line-height: 1;
  }
  .name-last {
    color: var(--white);
    font-weight: 700;
    font-size: 38px;
    line-height: 1.05;
  }
  .tagline {
    color: var(--gold-soft);
    font-size: 17px;
    margin-top: 6px;
  }
</style>
</head>
<body>
  <main class="stage">
    <section class="card card-back">
      <div class="contact-panel">
        <p class="contact-phone">555.310.4827</p>
        <p class="contact-email">hello@arvelointeriors.com</p>
      </div>
    </section>

    <section class="card card-front">
      <div class="dot-pattern" role="img" aria-label="Gold halftone dot zigzag pattern on blush pink"></div>
      <div class="name-panel">
        <p class="name-first">Lucía</p>
        <p class="name-last">Arvelo</p>
        <p class="tagline">interior decor</p>
      </div>
    </section>
  </main>
</body>
</html>
```